Business card design needed

It's a new business in town.Something so the name stands out.I need a logo for the B.R.K
I may all so use the design as a sign on a building

Contact Information for Business Card

B.R.K
Brackenvale Auto Detailing
42 Tillbury Crs
Brackenvale Vic 3819
Ph:(03)58264027
Mob:0417392658

```html
<!DOCTYPE html>
<html lang="en">
<head>
<meta charset="utf-8">
<title>Brackenvale Auto Detailing – Business Cards</title>
<link rel="stylesheet" href="https://fonts.googleapis.com/css2?family=Source+Sans+3:wght@300;400&display=swap">
<style>
  :root {
    --page-bg: #ffffff;
    --panel: #3a464c;
    --card-light: #5d727c;
    --card-mid: #4a5a62;
    --card-dark: #363f44;
    --ink: #ffffff;
    --text-font: "Source Sans 3", "Myriad Pro", Arial, sans-serif;
  }
  html, body {
    margin: 0;
    padding: 0;
    width: 1200px;
    height: 1200px;
    overflow: hidden;
    background: var(--page-bg);
  }
  .sheet {
    position: relative;
    width: 1200px;
    height: 1200px;
    font-family: var(--text-font);
    color: var(--ink);
  }
  .side-panel {
    position: absolute;
    left: 732px;
    top: 0;
    width: 468px;
    height: 1200px;
    background: var(--panel);
  }
  .card {
    position: absolute;
    left: 86px;
    width: 558px;
    height: 321px;
    background: linear-gradient(115deg, var(--card-light) 0%, var(--card-mid) 45%, var(--card-dark) 100%);
    overflow: hidden;
  }
  .card--vertical { top: 107px; }
  .card--horizontal { top: 444px; }
  .card--front { top: 777px; }

  .brand-name {
    position: absolute;
    font-family: var(--text-font);
    font-weight: 300;
    color: var(--ink);
    line-height: 1;
    white-space: nowrap;
  }
  .card--vertical .brand-name {
    left: 70px;
    top: 72px;
    height: 180px;
    font-size: 66px;
    writing-mode: vertical-rl;
    transform: rotate(180deg);
    text-align: center;
  }
  .card--horizontal .brand-name {
    left: 62px;
    top: 120px;
    width: 210px;
    font-size: 78px;
    text-align: center;
  }
  .card--front .brand-name {
    left: 0;
    width: 558px;
    top: 60px;
    font-size: 150px;
    text-align: center;
  }
  .tagline {
    position: absolute;
    left: 0;
    width: 558px;
    top: 212px;
    text-align: center;
    font-weight: 300;
    font-size: 22px;
    letter-spacing: 2px;
    text-transform: lowercase;
    word-spacing: 10px;
  }

  .divider {
    position: absolute;
    width: 2px;
    background: var(--ink);
  }
  .card--vertical .divider { left: 153px; top: 73px; height: 188px; }
  .card--horizontal .divider { left: 278px; top: 69px; height: 189px; }

  .contact {
    position: absolute;
    margin: 0;
    font-size: 16px;
    font-weight: 400;
    line-height: 21px;
    font-style: normal;
  }
  .contact p { margin: 0; }
  .contact p + p { margin-top: 21px; }
  .card--vertical .contact { left: 172px; top: 88px; }
  .card--horizontal .contact { left: 297px; top: 91px; }
</style>
</head>
<body>
<main class="sheet">
  <section class="card card--vertical" aria-label="Business card, vertical name layout">
    <div class="brand-name">B.R.K</div>
    <span class="divider"></span>
    <address class="contact">
      <p>Brackenvale Auto Detailing</p>
      <p>42 Tillbury Crs<br>Brackenvale Vic 3819</p>
      <p>Telephone: (03)58264027<br>Mobile: 0417392658</p>
    </address>
  </section>

  <section class="card card--horizontal" aria-label="Business card, horizontal name layout">
    <div class="brand-name">B.R.K</div>
    <span class="divider"></span>
    <address class="contact">
      <p>Brackenvale Auto Detailing</p>
      <p>42 Tillbury Crs<br>Brackenvale Vic 3819</p>
      <p>Telephone: (03)58264027<br>Mobile: 0417392658</p>
    </address>
  </section>

  <section class="card card--front" aria-label="Business card front">
    <div class="brand-name">B.R.K</div>
    <div class="tagline">Brackenvale Auto Detailing</div>
  </section>

  <aside class="side-panel"></aside>
</main>
</body>
</html>
```